KB Rubbish Removal Business Card

Hey,
I need a double sided business card designed for a rubbish removal business based in Australia. Logo is already chosen, similar colours preferred for both sides of the business card.

Details to include:

Front:

KB Rubbish Removal
Darren Holloway
Managing Director
Mobile: 0471 902 146
Email: darren@kbrubbishremoval.com.au
Website: kbrubbishremoval.com.au

Rear:

How did we do?
kbrubbishremoval.com.au/review

```html
<!DOCTYPE html>
<html lang="en">
<head>
<meta charset="utf-8">
<title>KB Rubbish Removal Business Card</title>
<link rel="stylesheet" href="https://fonts.googleapis.com/css2?family=Archivo:wght@400;600;700&display=swap">
<style>
  :root {
    --backdrop: #1d1c1b;
    --card: #070807;
    --green: #3fb64b;
    --green-deep: #23903a;
    --green-text: #2ea445;
    --green-faint: rgba(63, 182, 75, 0.07);
  }
  * { margin: 0; padding: 0; box-sizing: border-box; }
  html, body {
    width: 1200px;
    height: 927px;
    overflow: hidden;
    background: var(--backdrop);
    font-family: "Archivo", Arial, sans-serif;
  }
  .canvas { position: relative; width: 1200px; height: 927px; }
  .card {
    position: absolute;
    width: 560px;
    height: 320px;
    background: var(--card);
    border-radius: 14px;
    overflow: hidden;
    box-shadow: 0 18px 40px rgba(0, 0, 0, 0.55);
  }
  .card--front { left: 80px; top: 90px; }
  .card--back { left: 560px; top: 500px; }

  .brand {
    display: flex;
    align-items: center;
    gap: 14px;
    color: var(--green);
    font-weight: 700;
    white-space: nowrap;
  }
  .brand__dot { flex: none; border-radius: 50%; background: var(--green); }

  /* front: brand name and review prompt */
  .front-stack {
    position: absolute;
    left: 50%;
    top: 50%;
    transform: translate(-50%, -50%);
    display: flex;
    flex-direction: column;
    align-items: center;
    gap: 28px;
  }
  .card--front .brand { font-size: 34px; }
  .card--front .brand__dot { width: 40px; height: 40px; }
  .review { text-align: center; color: var(--green-text); }
  .review__prompt { font-size: 20px; font-weight: 600; }
  .review__link { font-size: 16px; margin-top: 6px; }

  /* back: faint decoration */
  .faint-circle {
    position: absolute;
    right: -90px;
    top: -40px;
    width: 280px;
    height: 280px;
    border-radius: 50%;
    background: var(--green-faint);
  }
  .card--back .brand {
    position: absolute;
    left: 40px;
    top: 44px;
    font-size: 20px;
    gap: 10px;
  }
  .card--back .brand__dot { width: 24px; height: 24px; }

  .contact { position: absolute; left: 40px; top: 150px; color: var(--green-text); z-index: 1; }
  .contact__name { font-size: 22px; font-weight: 700; color: var(--green-deep); }
  .contact__role { font-size: 16px; margin-top: 4px; margin-left: 8px; }
  .contact__list { list-style: none; margin-top: 8px; }
  .contact__item {
    display: flex;
    align-items: center;
    gap: 9px;
    font-size: 16px;
    line-height: 1.6;
    margin-left: 8px;
    white-space: nowrap;
  }
  .contact__icon { width: 14px; height: 14px; fill: var(--green-text); flex: none; }
</style>
</head>
<body>
<main class="canvas">
  <section class="card card--front" aria-label="Card front">
    <div class="front-stack">
      <div class="brand"><span class="brand__dot"></span><span>KB Rubbish Removal</span></div>
      <div class="review">
        <p class="review__prompt">How did we do?</p>
        <p class="review__link">kbrubbishremoval.com.au/review</p>
      </div>
    </div>
  </section>

  <section class="card card--back" aria-label="Card back">
    <div class="faint-circle"></div>
    <div class="brand"><span class="brand__dot"></span><span>KB Rubbish Removal</span></div>
    <div class="contact">
      <h1 class="contact__name">Darren Holloway</h1>
      <p class="contact__role">Managing Director</p>
      <ul class="contact__list">
        <li class="contact__item">
          <svg class="contact__icon" viewBox="0 0 24 24"><path d="M6.6 10.8a15.1 15.1 0 0 0 6.6 6.6l2.2-2.2c.3-.3.7-.4 1-.2 1.1.4 2.3.6 3.6.6.6 0 1 .4 1 1V20c0 .6-.4 1-1 1A17 17 0 0 1 3 4c0-.6.4-1 1-1h3.5c.6 0 1 .4 1 1 0 1.3.2 2.5.6 3.6.1.3 0 .7-.2 1z"/></svg>
          <span>0471 902 146</span>
        </li>
        <li class="contact__item">
          <svg class="contact__icon" viewBox="0 0 24 24"><path d="M2 5h20v14H2z M2 5l10 8 10-8" fill="none" stroke="#2ea445" stroke-width="2.4"/></svg>
          <span>darren@kbrubbishremoval.com.au</span>
        </li>
        <li class="contact__item">
          <svg class="contact__icon" viewBox="0 0 24 24"><circle cx="12" cy="12" r="10" fill="none" stroke="#2ea445" stroke-width="2.4"/><path d="M2 12h20M12 2c3 3 3 17 0 20M12 2c-3 3-3 17 0 20" fill="none" stroke="#2ea445" stroke-width="1.8"/></svg>
          <span>kbrubbishremoval.com.au</span>
        </li>
      </ul>
    </div>
  </section>
</main>
</body>
</html>
```